Summit Grading a Builders LLC business card

My current business card is very plain. it has my logo and contact information. I woud like something that stands out from the rest. please take a look at my website to see about my company.

Compayt Name - Summit Grading And Builders
Owner - Martin Kowalczyk
Business Address
Business Website - www.summitgradingandbuilders.example
Email - Summitgradingandbuilders@mailbox.example
Phone - 555-214-7390
Fax - 555-806-3127

Target Market(s)

Everyone age tang is 18 - 85

Industry/Entity Type

Business

Contact Information for Business Card

Nice and professional all in one.

Font styles to use
Serif
Other font styles liked:
• Up to you

Requirements
Must have
• All contact info. The design is up to you.
Nice to have
• All the contact info the design is up to you
Should not have
• I don't have any

```html
<!DOCTYPE html>
<html lang="en">
<head>
<meta charset="utf-8">
<title>Summit Grading &amp; Builders LLC — Business Card</title>
<link href="https://fonts.googleapis.com/css2?family=EB+Garamond:wght@400;600&display=swap" rel="stylesheet">
<style>
  :root {
    --page-bg: #e6e6e4;
    --card-front: #efefef;
    --card-back: #444444;
    --brand-ink: #3a3a3a;
    --brand-ink-faint: #565656;
    --accent-green: #1f7a1f;
    --shadow: rgba(0,0,0,0.28);
  }
  * { margin: 0; padding: 0; box-sizing: border-box; }
  html, body {
    width: 1200px; height: 1000px; overflow: hidden;
    background: var(--page-bg);
    font-family: "EB Garamond", Georgia, serif;
  }
  .card {
    position: absolute;
    left: 280px;
    width: 640px;
    height: 345px;
    box-shadow: 0 10px 24px var(--shadow);
  }
  .card--front { top: 110px; background: var(--card-front); }
  .card--back  { top: 540px; background: var(--card-back); }

  .brand-name {
    position: absolute;
    left: 0; right: 0;
    text-align: center;
    font-weight: 600;
    text-transform: uppercase;
    letter-spacing: 1px;
    line-height: 1.05;
  }
  .card--front .brand-name {
    top: 36px;
    font-size: 34px;
    color: var(--brand-ink);
    padding-left: 40px;
  }
  .card--back .brand-name {
    top: 110px;
    font-size: 40px;
    color: var(--brand-ink-faint);
  }

  .owner {
    position: absolute;
    left: 330px;
    top: 158px;
    width: 170px;
    text-align: center;
    color: var(--accent-green);
  }
  .owner__name { font-size: 20px; line-height: 1.1; }
  .owner__title { font-size: 15px; line-height: 1.1; }

  .contact-list {
    position: absolute;
    left: 326px;
    top: 206px;
    list-style: none;
    color: var(--accent-green);
    font-size: 12.5px;
  }
  .contact-list li {
    display: flex;
    align-items: center;
    height: 22px;
  }
  .contact-list svg {
    width: 17px; height: 17px;
    margin-right: 10px;
    flex: none;
    fill: var(--accent-green);
  }
</style>
</head>
<body>
  <section class="card card--front" aria-label="Business card front">
    <div class="brand-name">Summit Grading<br>&amp; Builders LLC</div>

    <div class="owner">
      <div class="owner__name">Martin Kowalczyk</div>
      <div class="owner__title">Owner</div>
    </div>

    <ul class="contact-list">
      <li>
        <svg viewBox="0 0 20 20" aria-hidden="true"><circle cx="10" cy="10" r="10"/><path d="M6.5 5h2l1 2.5-1.3 1a6 6 0 0 0 3.3 3.3l1-1.3 2.5 1v2c0 .6-.5 1-1 1A9 9 0 0 1 5.5 6c0-.5.4-1 1-1z" fill="#efefef"/></svg>
        555-214-7390
      </li>
      <li>
        <svg viewBox="0 0 20 20" aria-hidden="true"><rect x="2" y="7" width="16" height="11" rx="1.5"/><rect x="5" y="2" width="8" height="6"/><rect x="11" y="10" width="5" height="1.5" fill="#efefef"/><rect x="11" y="13" width="5" height="1.5" fill="#efefef"/><rect x="4" y="10" width="5" height="6" fill="#efefef"/></svg>
        555-806-3127
      </li>
      <li>
        <svg viewBox="0 0 20 20" aria-hidden="true"><path d="M10 1a6.5 6.5 0 0 0-6.5 6.5C3.5 12 10 19 10 19s6.5-7 6.5-11.5A6.5 6.5 0 0 0 10 1z"/><circle cx="10" cy="7.5" r="2.3" fill="#efefef"/></svg>
        4870 Ridgeline Avenue, Millbrook, NY, United States
      </li>
      <li>
        <svg viewBox="0 0 20 20" aria-hidden="true"><rect x="1" y="4" width="18" height="12"/><path d="M1.5 4.5 10 11l8.5-6.5" fill="none" stroke="#efefef" stroke-width="1.5"/></svg>
        Summitgradingandbuilders@mailbox.example
      </li>
      <li>
        <svg viewBox="0 0 20 20" aria-hidden="true"><circle cx="10" cy="10" r="9"/><g fill="none" stroke="#efefef" stroke-width="1.1"><circle cx="10" cy="10" r="6.5"/><ellipse cx="10" cy="10" rx="3" ry="6.5"/><path d="M3.5 10h13M4.5 6.8h11M4.5 13.2h11"/></g></svg>
        www.summitgradingandbuilders.example
      </li>
    </ul>
  </section>

  <section class="card card--back" aria-label="Business card back">
    <div class="brand-name">Summit Grading<br>&amp; Builders LLC</div>
  </section>
</body>
</html>
```